Design outside banner for my business

We are looking for someone to design a promotional banner we will put in different places in our city to promote our car finance business. Important that we keep a white background. Size is 96 inches wide by 48 inches high

Requirements
Must have
• White background and large logo
Should not have
• Small text

```html
<!DOCTYPE html>
<html lang="fr">
<head>
<meta charset="utf-8">
<title>Nova Auto Crédit – Bannière</title>
<link href="https://fonts.googleapis.com/css2?family=Roboto:wght@400;500;700;900&family=Open+Sans:wght@300;400&display=swap" rel="stylesheet">
<style>
  :root {
    --stage: #000000;
    --paper: #ffffff;
    --ink: #1a1a1a;
    --brand-red: #b5302c;
    --rule: #c9605c;
    --caption: #bdbdbd;
    --photo-warm: #d9c2ae;
    --photo-cool: #e4e6ea;
  }
  * { box-sizing: border-box; margin: 0; padding: 0; }
  html, body { width: 1200px; height: 1200px; overflow: hidden; background: var(--stage); }
  .stage { position: relative; width: 1200px; height: 1200px; background: var(--stage); font-family: "Roboto", Arial, sans-serif; }

  .banner { position: absolute; left: 62px; top: 322px; width: 1076px; height: 538px; background: var(--paper); overflow: hidden; }

  .hero-photo {
    position: absolute; left: 0; top: 0; width: 660px; height: 538px;
    background:
      radial-gradient(ellipse 150px 260px at 140px 230px, var(--photo-warm) 0%, rgba(217,194,174,0.55) 55%, rgba(217,194,174,0) 100%),
      linear-gradient(90deg, var(--photo-cool) 0%, rgba(228,230,234,0.7) 45%, rgba(255,255,255,0) 100%);
  }

  .brand { position: absolute; right: 34px; top: 74px; display: flex; align-items: center; gap: 10px; }
  .brand-mark { width: 24px; height: 24px; border-radius: 50%; background: var(--brand-red); }
  .brand-name { font-weight: 900; font-size: 32px; line-height: 1; color: var(--ink); letter-spacing: 0.5px; }

  .headline p { position: absolute; left: 256px; line-height: 1; font-weight: 700; color: var(--ink); white-space: nowrap; }
  .headline-lead { top: 136px; font-size: 28.5px; }
  .headline-main { top: 164px; font-size: 75px; color: var(--brand-red) !important; letter-spacing: -0.5px; }
  .headline-sub { top: 230px; font-size: 29px; letter-spacing: -0.2px; }

  .offer { position: absolute; left: 424px; top: 279px; width: 290px; text-align: center; }
  .offer-tiers { font-size: 28px; font-weight: 700; color: var(--brand-red); line-height: 30px; border-bottom: 1px solid var(--rule); }
  .offer-line { font-size: 21px; line-height: 25px; color: var(--ink); border-bottom: 1px solid var(--rule); white-space: nowrap; }

  .situations { position: absolute; left: 181px; top: 383px; width: 880px; height: 70px; list-style: none; }
  .situations li { position: absolute; font-size: 19px; line-height: 22px; color: var(--ink); display: flex; align-items: center; gap: 6px; white-space: nowrap; }
  .situations .situation-narrow { letter-spacing: -0.75px; }
  .situations svg { width: 18px; height: 18px; flex: none; }

  .contact { position: absolute; left: 181px; top: 464px; color: var(--ink); }
  .contact-label { font-size: 18px; line-height: 1; }
  .contact-phone { font-size: 25px; line-height: 1; color: var(--brand-red); margin-top: 1px; }
  .website { position: absolute; right: 34px; top: 486px; font-size: 20px; line-height: 1; color: var(--ink); }

  .caption { position: absolute; left: 0; width: 1200px; top: 918px; text-align: center; font-family: "Open Sans", Arial, sans-serif; font-weight: 300; font-size: 29px; color: var(--caption); }
</style>
</head>
<body>
<div class="stage">
  <section class="banner">
    <div class="hero-photo" role="img" aria-label="Photo d'une main tendant une clé de voiture"></div>

    <div class="brand">
      <span class="brand-mark"></span>
      <span class="brand-name">NOVA AUTO CRÉDIT</span>
    </div>

    <div class="headline">
      <p class="headline-lead">ROULER DANS VOTRE</p>
      <p class="headline-main">NOUVEAU VÉHICULE</p>
      <p class="headline-sub">EN 48 HEURES! TOUTES LES MARQUES DISPONIBLES</p>
    </div>

    <div class="offer">
      <p class="offer-tiers">1RE, 2E, 3E</p>
      <p class="offer-line">Chance Au Crédit Financement</p>
      <p class="offer-line">Automobile Aucun Cas Refusé</p>
    </div>

    <svg width="0" height="0" style="position:absolute">
      <symbol id="tick" viewBox="0 0 18 18">
        <rect x="1" y="3" width="13" height="13" fill="none" stroke="#b5302c" stroke-width="1.6"/>
        <path d="M4 9.5 L7.5 13 L16 1.5" fill="none" stroke="#1a1a1a" stroke-width="2"/>
      </symbol>
    </svg>
    <ul class="situations">
      <li style="left:0;top:0"><svg><use href="#tick"/></svg>Proposition au consommateur</li>
      <li style="left:296px;top:0"><svg><use href="#tick"/></svg>Remise volontaire</li>
      <li style="left:484px;top:0"><svg><use href="#tick"/></svg>Retards de paiements</li>
      <li style="left:704px;top:0"><svg><use href="#tick"/></svg>Recouvrements</li>
      <li class="situation-narrow" style="left:0;top:34px"><svg><use href="#tick"/></svg>Récemment travailleur autonome</li>
      <li style="left:296px;top:34px"><svg><use href="#tick"/></svg>Faible revenu</li>
      <li style="left:484px;top:34px"><svg><use href="#tick"/></svg>Faillitea</li>
      <li style="left:704px;top:34px"><svg><use href="#tick"/></svg>Mauvais crédit</li>
    </ul>

    <div class="contact">
      <p class="contact-label">Contactez-nous au</p>
      <p class="contact-phone">514-555-0142 ext.0</p>
    </div>
    <p class="website">www.novaautocredit.com</p>
  </section>

  <p class="caption">Banner size 96″ x 48″</p>
</div>
</body>
</html>
```